Wine Bottle Lable

Want a unique, simple but elegant, label for a wine bottle. I want to use the letters "TWG" in the design which is a moniker for my last name "Tallwidge". The letters TWG do not have to be juxtaposed together so that it is recognizable, or they could be something like T-WG, WG-T, TGW T-WG-T, etc. The X could be totally separated from the NO, or otherwise. The wine is a white wine in a clear bottle. I need Adobe Illustrator files so I can add the wine varietal, year, alcohol content. The label should be 4" wide and 5" tall.

Colors

Designer to choose colors to be used in the design.

Requirements
Nice to have
• outstanding but simple graphics

```html
<!DOCTYPE html>
<html lang="en">
<head>
<meta charset="utf-8">
<title>Tallwidge Sauvignon Blanc 2019 Label</title>
<link rel="stylesheet" href="https://fonts.googleapis.com/css2?family=Josefin+Sans:ital,wght@0,300;1,300&family=Libre+Baskerville:wght@700&display=swap">
<style>
  :root {
    --paper: #ffffff;
    --ink: #1c1c1c;
    --gold: #d6ab2e;
  }
  html, body {
    margin: 0;
    padding: 0;
    width: 960px;
    height: 1200px;
    overflow: hidden;
    background: var(--paper);
  }
  .label {
    position: relative;
    width: 960px;
    height: 1200px;
    background: var(--paper);
    color: var(--ink);
  }
  .label > * {
    position: absolute;
    left: 0;
    width: 100%;
    margin: 0;
    text-align: center;
  }
  .brand-mark {
    top: 210px;
    display: flex;
    justify-content: center;
    align-items: center;
    gap: 28px;
    height: 110px;
  }
  .brand-mark__dot {
    width: 44px;
    height: 44px;
    border-radius: 50%;
    background: var(--gold);
  }
  .brand-mark__letters {
    font-family: "Josefin Sans", "Helvetica Neue", sans-serif;
    font-weight: 300;
    font-size: 84px;
    line-height: 1;
    letter-spacing: 8px;
    color: var(--ink);
    padding-top: 14px;
  }
  .brand-name {
    top: 474px;
    font-family: "Libre Baskerville", Georgia, serif;
    font-weight: 700;
    font-size: 26px;
    letter-spacing: 9px;
    padding-left: 9px;
    box-sizing: border-box;
    line-height: 1;
  }
  .varietal {
    top: 740px;
    font-family: "Josefin Sans", "Helvetica Neue", sans-serif;
    font-weight: 300;
    font-size: 66px;
    letter-spacing: 5px;
    line-height: 1;
  }
  .vintage {
    top: 898px;
    font-family: "Josefin Sans", "Helvetica Neue", sans-serif;
    font-weight: 300;
    font-size: 38px;
    letter-spacing: 2px;
    line-height: 1;
  }
  .abv {
    top: 1098px;
    font-family: "Josefin Sans", "Helvetica Neue", sans-serif;
    font-weight: 300;
    font-style: italic;
    font-size: 29px;
    line-height: 1;
  }
</style>
</head>
<body>
  <main class="label">
    <div class="brand-mark">
      <span class="brand-mark__dot" aria-hidden="true"></span>
      <span class="brand-mark__letters">T-WG</span>
    </div>
    <p class="brand-name">TALLWIDGE</p>
    <h1 class="varietal" style="font-weight:300">Sauvignon Blanc</h1>
    <p class="vintage">2019</p>
    <p class="abv">10% vol</p>
  </main>
</body>
</html>
```